Edgy rebranded biz cards KRB

We are rebranding our 20 yr old mortgage company with a new logo and would like cards to compliment our new look.

Target Market(s)

potential home buyers or clients for refinance

Industry/Entity Type

Mortgage Brokerage

Contact Information for Business Card

418 W. Lomita Ave #305
Henderson, NV 89152
702.519.4827 o
702-519-4829 f
www.kestrelridgelending,example
nmls 842019
KRB is an equal housing lender

Font styles to use
Sans Serif

Colors
0455a3
3176b5
0393ce
33a6d7

Requirements
Must have
• space for a photo
Nice to have
• One side with the company info and the other with the person's info

```html
<!DOCTYPE html>
<html lang="en">
<head>
<meta charset="utf-8">
<title>Kestrel Ridge Lending – Business Card</title>
<link href="https://fonts.googleapis.com/css2?family=Fira+Sans:wght@400;600;700&display=swap" rel="stylesheet">
<style>
  :root {
    --page-bg: #e4e4e4;
    --brand-blue: #0a6fb5;
    --brand-deep: #0455a3;
    --card-light: #f4f4f4;
    --ink: #2b2b2b;
    --band-gray: #8a8c8e;
    --white: #ffffff;
  }
  * { margin: 0; padding: 0; box-sizing: border-box; }
  html, body {
    width: 1200px; height: 960px; overflow: hidden;
    background: var(--page-bg);
    font-family: "Fira Sans", Arial, sans-serif;
  }
  .canvas { position: relative; width: 1200px; height: 960px; }

  .card {
    position: absolute; left: 309px; width: 593px; height: 339px; overflow: hidden;
  }

  /* Front */
  .card-front { top: 125px; background: var(--brand-blue); color: var(--white); }
  .front-wordmark {
    position: absolute; left: 0; right: 0; top: 250px;
    text-align: center; font-weight: 600; font-size: 44px; letter-spacing: 1px; line-height: 1.05;
  }
  .front-wordmark span { display: block; }
  .lender-note {
    position: absolute; left: 0; right: 0; top: 289px;
    text-align: center; font-size: 14.5px; letter-spacing: 0.3px;
  }
  .lender-note b { font-weight: 700; }

  /* Back */
  .card-back { top: 516px; background: var(--card-light); }
  .portrait {
    position: absolute; left: 12px; top: 18px; width: 280px; height: 294px;
    background: linear-gradient(180deg, #e9e9ea 0%, #d3d4d7 55%, #2b3342 100%);
  }
  .info {
    position: absolute; left: 310px; width: 258px; top: 34px; text-align: center;
  }
  .back-wordmark {
    color: var(--brand-blue); font-weight: 600; font-size: 29px; line-height: 1.08; letter-spacing: 0.5px;
  }
  .person-name {
    margin-top: 22px; color: var(--brand-blue); font-weight: 700; font-size: 19px; letter-spacing: 0.6px;
  }
  .person-role { margin-top: 4px; font-size: 14px; color: var(--ink); letter-spacing: 0.4px; }
  .icon-rule { margin-top: 12px; display: block; margin-left: auto; margin-right: auto; }
  .contact-list { list-style: none; margin-top: 4px; font-size: 14.5px; color: var(--ink); line-height: 20px; }
  .contact-list b { color: var(--brand-blue); font-weight: 700; }

  .footer-band { position: absolute; left: 0; bottom: 0; width: 593px; height: 28px; }
  .footer-band svg { position: absolute; left: 0; top: 0; }
  .address {
    position: absolute; left: 34px; top: 5px; font-size: 14px; color: var(--white);
  }
  .license {
    position: absolute; right: 43px; top: 5px; font-size: 14px; color: var(--white);
  }
</style>
</head>
<body>
<main class="canvas">

  <section class="card card-front">
    <div class="front-wordmark" style="top:100px"><span>KESTREL RIDGE</span><span>LENDING</span></div>
    <p class="lender-note"><b>KRB</b> IS AN EQUAL HOUSING LENDER</p>
  </section>

  <section class="card card-back">
    <div class="portrait" role="img" aria-label="Portrait photo of the loan officer in a dark suit"></div>

    <div class="info">
      <div class="back-wordmark">KESTREL RIDGE<br>LENDING</div>
      <h1 class="person-name">DANIEL WHITAKER</h1>
      <p class="person-role">BROKERAGE</p>

      <svg class="icon-rule" width="186" height="18" viewBox="0 0 186 18" aria-hidden="true">
        <line x1="0" y1="9" x2="186" y2="9" stroke="#555" stroke-width="1"/>
        <g fill="var(--brand-blue)">
          <circle cx="62" cy="9" r="8"/><circle cx="82" cy="9" r="8"/>
          <circle cx="102" cy="9" r="8"/><circle cx="122" cy="9" r="8"/>
        </g>
        <g fill="none" stroke="#fff" stroke-width="1.4" stroke-linecap="round">
          <path d="M58.5 5.5 q0 6 7 7 l1-2 -2-1.5 -1.2 1 q-2-1-2.8-2.8 l1-1.2 -1.5-2 z" fill="#fff" stroke="none"/>
          <rect x="78" y="7" width="8" height="5"/><rect x="79.5" y="4.5" width="5" height="2.5"/>
          <rect x="98" y="5.5" width="8" height="7"/><path d="M98 5.5 l4 3.5 4-3.5"/>
          <circle cx="122" cy="9" r="4.5"/><path d="M117.5 9 h9 M122 4.5 q-3 4.5 0 9 q3-4.5 0-9"/>
        </g>
      </svg>

      <ul class="contact-list">
        <li>702.519.4827</li>
        <li>702-519-4829</li>
        <li>daniel@kestrelridgelending,example</li>
        <li>www.<b>kestrelridgelending</b>,example</li>
      </ul>
    </div>

    <div class="footer-band">
      <svg width="593" height="28" viewBox="0 0 593 28" aria-hidden="true">
        <polygon points="395,0 593,0 593,28 410,28" fill="var(--band-gray)"/>
        <polygon points="0,0 398,0 410,28 0,28" fill="var(--brand-blue)"/>
      </svg>
      <span class="address">418 W. Lomita Ave #305, Henderson, NV 89152</span>
      <span class="license">nmls 842019</span>
    </div>
  </section>

</main>
</body>
</html>
```